Accounting company website and Facebook page design

I need a website designed and copy written for an accounting/bookkeeping company in Ohio. We have content but would need someone to fine-tune it and make it sound good. I also need a Facebook page design created. Attached is the logo for the company.

```html
<!DOCTYPE html>
<html lang="en">
<head>
<meta charset="utf-8">
<title>Keystone Ledger Group, Inc — Accounting, Bookkeeping and Tax Prep</title>
<link rel="stylesheet" href="https://fonts.googleapis.com/css2?family=Cinzel:wght@400;600;700;800&family=Roboto:wght@300;400;500&display=swap">
<style>
:root{
  --gold:#eaa623;
  --gold-soft:#f2c25a;
  --ink:#111111;
  --text:#333333;
  --muted:#9a9a9a;
  --paper:#ffffff;
  --mist:#f4f4f4;
  --night:#0b0b0b;
  --head:'Cinzel',serif;
  --body:'Roboto',sans-serif;
}
*{margin:0;padding:0;box-sizing:border-box}
html,body{width:1200px;height:3613px;overflow:hidden}
body{position:relative;background:var(--paper);font-family:var(--body);color:var(--text)}
.abs{position:absolute}
a{color:inherit;text-decoration:none}

/* header */
.site-header{position:absolute;left:0;top:0;width:1200px;height:101px;background:var(--paper);z-index:5}
.brand{position:absolute;left:115px;top:22px;display:flex;align-items:center;gap:10px;font-family:var(--head);font-weight:700;font-size:26px;color:var(--ink);letter-spacing:1px}
.brand-dot{width:14px;height:14px;border-radius:50%;background:var(--gold)}
.topbar{position:absolute;left:456px;top:0;width:602px;height:38px}
.topbar svg{position:absolute;left:0;top:0}
.topbar-items{position:absolute;left:60px;top:0;height:38px;display:flex;align-items:center;gap:26px;color:#fff;font-size:15px}
.topbar-items span{display:flex;align-items:center;gap:8px}
.nav{position:absolute;top:60px;left:0;font-size:15px;color:var(--text)}
.nav a{position:absolute;white-space:nowrap}
.nav a.active{color:var(--gold)}
.nav-underline{position:absolute;left:470px;top:97px;width:36px;height:3px;background:var(--gold)}

/* hero */
.hero-photo{position:absolute;left:0;top:101px;width:1200px;height:710px;background:linear-gradient(100deg,#f3ece0 0%,#efe3cd 40%,#d9d2c6 70%,#cfc8bc 100%)}
.hero-edge{position:absolute;left:0;top:640px}
.hero-kicker{position:absolute;left:112px;top:262px;font-family:var(--body);font-weight:300;font-size:40px;color:var(--gold);letter-spacing:1px}
.hero-title{position:absolute;left:110px;top:312px;font-family:var(--head);font-weight:800;font-size:58px;line-height:75px;color:var(--ink)}
.hero-copy{position:absolute;left:112px;top:462px;width:460px;font-size:15px;line-height:26px;color:var(--text)}
.btn{position:absolute;display:flex;align-items:center;justify-content:center;background:var(--gold);color:#fff;border-radius:28px;font-family:var(--head);font-weight:700;font-size:15px;letter-spacing:.5px}

/* shared headings */
.h2{position:absolute;font-family:var(--head);font-weight:700;font-size:34px;color:var(--ink);letter-spacing:.5px}
.rule{position:absolute;height:2px;width:70px;background:var(--gold)}

/* about */
.about-burst{position:absolute;left:77px;top:870px;width:526px;height:410px;background:radial-gradient(ellipse at 50% 50%,#f6e3b6 0%,rgba(246,227,182,.4) 45%,rgba(255,255,255,0) 72%)}
.photo{position:absolute;background:linear-gradient(135deg,#cfc6bb,#8f8a86)}
.photo.framed{border:5px solid #fff;box-shadow:0 4px 14px rgba(0,0,0,.12)}
.about-copy{position:absolute;left:621px;top:1012px;width:450px;font-size:15px;line-height:25.7px;color:var(--text)}

/* services */
.services{position:absolute;left:0;top:1373px;width:1200px;height:604px;background:linear-gradient(90deg,#eaa623 0%,#e9a628 55%,#d99a2a 100%)}
.services-photo{position:absolute;left:760px;top:1373px;width:440px;height:604px;background:linear-gradient(90deg,rgba(234,166,35,0),rgba(150,105,40,.25))}
.service-img{position:absolute;top:1593px;width:306px;height:230px;border-radius:4px;background:linear-gradient(135deg,#d8d3cc,#7f7a74)}
.service-label{position:absolute;top:1797px;width:244px;height:89px;background:#fff;border-radius:4px;text-align:center}
.service-label h3{font-family:var(--head);font-weight:700;font-size:20px;color:var(--ink);margin-top:14px}
.service-label p{font-family:var(--head);font-weight:700;font-size:12px;color:var(--gold);margin-top:6px;letter-spacing:.5px}

/* testimonials */
.review-card{position:absolute;left:430px;top:2141px;width:323px;height:327px;background:#fff;border-radius:18px;box-shadow:0 6px 30px rgba(0,0,0,.08)}
.review{position:absolute;top:2176px;width:290px}
.stars{display:flex;gap:8px;margin-bottom:14px}
.review p{font-size:15px;line-height:25.7px;color:var(--muted)}
.author{position:absolute;top:2380px;display:flex;align-items:center;gap:12px}
.avatar{width:50px;height:50px;border-radius:50%;background:linear-gradient(135deg,#c9b7a3,#6f6a66)}
.author b{display:block;font-family:var(--head);font-weight:700;font-size:14px;color:var(--ink)}
.author small{display:block;font-size:13px;color:var(--muted);margin-top:3px}

/* contact */
.contact{position:absolute;left:0;top:2554px;width:1200px;height:600px;background:var(--mist)}
.info-icon{position:absolute;left:114px;width:50px;height:50px;border-radius:50%;border:2px solid var(--gold);display:flex;align-items:center;justify-content:center;background:#fff}
.info-title{position:absolute;left:178px;font-family:var(--head);font-weight:700;font-size:21px;color:var(--ink)}
.info-text{position:absolute;left:178px;font-size:15px;line-height:24px;color:var(--ink);width:240px}
.field{position:absolute;left:437px;width:317px;height:52px;background:#fff;font-size:14px;color:var(--muted);padding:17px 24px}
.submit{position:absolute;left:437px;top:2920px;width:317px;height:52px;background:var(--gold);color:#fff;font-family:var(--head);font-weight:700;font-size:15px;display:flex;align-items:center;justify-content:center}
.message{position:absolute;left:775px;top:2716px;width:300px;height:256px;background:#fff;font-size:14px;color:var(--muted);padding:17px 24px}

/* footer */
.footer{position:absolute;left:0;top:3035px;width:1200px;height:578px;background:var(--night)}
.footer-edge{position:absolute;left:0;top:3035px}
.badge{position:absolute;width:60px;height:60px;border-radius:50%;background:#fff;display:flex;align-items:center;justify-content:center}
.badge i{width:16px;height:16px;border-radius:50%;background:var(--gold)}
.footer-brand{position:absolute;left:112px;top:3296px;display:flex;align-items:center;gap:10px;font-family:var(--head);font-weight:700;font-size:28px;color:#fff}
.social{position:absolute;top:3391px;width:32px;height:32px;border-radius:50%;background:#fff}
.social::after{content:"";position:absolute;left:11px;top:11px;width:10px;height:10px;border-radius:50%;background:var(--gold)}
.f-head{position:absolute;top:3258px;font-family:var(--head);font-weight:700;font-size:19px;color:#fff}
.f-rule{position:absolute;top:3291px;width:34px;height:2px;background:var(--gold)}
.f-links{position:absolute;top:3313px;list-style:none;font-size:15px;line-height:30px;color:#fff}
.f-text{position:absolute;left:763px;top:3312px;width:300px;font-size:15px;line-height:25px;color:#fff}
.subscribe{position:absolute;left:763px;top:3380px;width:274px;height:42px;border-radius:21px;background:#fff;font-size:14px;color:var(--muted);padding:12px 20px}
.subscribe-btn{position:absolute;left:991px;top:3378px;width:46px;height:46px;border-radius:50%;background:var(--gold);display:flex;align-items:center;justify-content:center}
.f-divider{position:absolute;left:112px;top:3523px;width:976px;height:1px;background:#2c2c2c}
.copyright{position:absolute;left:0;top:3558px;width:1200px;text-align:center;font-size:15px;color:#fff}
.copyright a{color:var(--gold);text-decoration:underline}
</style>
</head>
<body>

<!-- header -->
<header class="site-header">
  <div class="brand"><span class="brand-dot"></span>Keystone Ledger</div>
  <div class="topbar">
    <svg width="602" height="38" viewBox="0 0 602 38"><polygon points="0,0 602,0 580,38 22,38" fill="#eaa623"/></svg>
    <div class="topbar-items">
      <span><svg width="14" height="14" viewBox="0 0 24 24"><path fill="#fff" d="M6.6 10.8a15.1 15.1 0 0 0 6.6 6.6l2.2-2.2c.3-.3.7-.4 1-.2 1.1.4 2.3.6 3.6.6.6 0 1 .4 1 1V20c0 .6-.4 1-1 1A17 17 0 0 1 3 4c0-.6.4-1 1-1h3.5c.6 0 1 .4 1 1 0 1.3.2 2.5.6 3.6.1.3 0 .7-.2 1z"/></svg>+1 888 888 8888</span>
      <span><svg width="16" height="12" viewBox="0 0 16 12"><rect width="16" height="12" rx="1" fill="#fff"/><path d="M0 1l8 6 8-6" stroke="#eaa623" stroke-width="1.5" fill="none"/></svg>info@keystoneledgerinc.com</span>
      <span><svg width="14" height="14" viewBox="0 0 14 14"><path d="M1 7h8M6 3.5L9.5 7 6 10.5" stroke="#fff" stroke-width="2" fill="none"/><path d="M9 1h4v12H9" stroke="#fff" stroke-width="2" fill="none"/></svg>Login</span>
    </div>
  </div>
  <nav class="nav">
    <a class="active" style="left:468px">Home</a>
    <a style="left:543px">About Us</a>
    <a style="left:639px">Our Services</a>
    <a style="left:763px">Who we Are</a>
    <a style="left:880px">Contact Us</a>
    <a style="left:991px">More</a>
  </nav>
  <div class="nav-underline"></div>
</header>

<!-- hero -->
<section>
  <div class="hero-photo" role="img" aria-label="Accountant in a striped shirt reviewing documents at a bright office desk with a laptop"></div>
  <svg class="hero-edge" width="1200" height="171" viewBox="0 640 1200 171">
    <polygon points="0,806 287,729 362,795 519,712 586,739 645,739 778,659 1200,806 1200,811 0,811" fill="#eaa623"/>
    <polygon points="0,811 287,742 362,808 519,726 586,752 645,752 778,674 1200,815 1200,811 0,811" fill="#fff"/>
  </svg>
  <div class="badge" style="left:583px;top:713px"><i></i></div>
  <div class="hero-kicker">WELCOME TO</div>
  <h1 class="hero-title">KEYSTONE LEDGER<br>GROUP, INC.</h1>
  <p class="hero-copy">Lorem ipsum dolor sit amet, consectetur adipiscing elit, sed do eiusmod tempor incididunt ut labore et dolore</p>
  <a class="btn" style="left:112px;top:529px;width:166px;height:56px">GET STARTED</a>
</section>

<!-- about -->
<section>
  <div class="about-burst"></div>
  <div class="photo" style="left:133px;top:879px;width:220px;height:224px" role="img" aria-label="Team meeting around a table with laptops"></div>
  <div class="photo framed" style="left:354px;top:953px;width:156px;height:155px" role="img" aria-label="Woman writing notes at a desk"></div>
  <div class="photo framed" style="left:242px;top:1103px;width:116px;height:119px" role="img" aria-label="Smiling woman holding binders in an office"></div>
  <div class="photo" style="left:360px;top:1108px;width:167px;height:171px" role="img" aria-label="Hands using a calculator beside a keyboard"></div>
  <h2 class="h2" style="left:621px;top:890px;line-height:45px">ABOUT KEYSTONE LEDGER<br>GROUP, INC</h2>
  <div class="rule" style="left:621px;top:990px"></div>
  <p class="about-copy">Lorem ipsum dolor sit amet, consectetur adipiscing elit, sed do eiusmod tempor incididunt ut labore et dolore magna aliqua. Quis ipsum suspendisse ultrices gravida. Risus commodo viverra maecenas accumsan lacus vel facilisis. Lorem ipsum dolor sit amet, consectetur adipiscing elit, sed do eiusmod tempor incididunt ut labore et dolore magna aliqua. Quis ipsum suspendisse ultrices gravida. Risus commodo viverra maecenas accumsan lacus vel facilisis. Lorem ipsum dolor sit amet,</p>
  <a class="btn" style="left:617px;top:1235px;width:165px;height:55px">LEARN MORE</a>
</section>

<!-- services -->
<section>
  <div class="services"></div>
  <div class="services-photo" role="img" aria-label="Faded photo of colleagues working together behind the section"></div>
  <h2 class="h2" style="left:0;width:1200px;text-align:center;top:1436px;color:#fff">OUR SERVICES</h2>
  <div class="rule" style="left:565px;top:1488px;background:#fff"></div>
  <p class="abs" style="left:300px;top:1508px;width:600px;text-align:center;color:#fff;font-size:15px;line-height:26px">Lorem ipsum dolor sit amet, consectetur adipiscing elit, sed do eiusmod tempor incididunt ut labore et dolore magna aliqua.</p>

  <div class="service-img" style="left:112px" role="img" aria-label="Hands working with a calculator and financial charts"></div>
  <div class="service-img" style="left:447px" role="img" aria-label="Man in glasses reviewing paperwork at a laptop"></div>
  <div class="service-img" style="left:782px" role="img" aria-label="Advisor holding a calculator during a client meeting"></div>
  <div class="service-label" style="left:140px"><h3>ACCOUNTING</h3><p>LEARN MORE</p></div>
  <div class="service-label" style="left:475px"><h3>BOOKKEEPING</h3><p>LEARN MORE</p></div>
  <div class="service-label" style="left:810px"><h3>TAXPREP</h3><p>LEARN MORE</p></div>
</section>

<!-- testimonials -->
<section>
  <h2 class="h2" style="left:0;width:1200px;text-align:center;top:2046px">WHAT PEOPLE ARE SAYING</h2>
  <div class="rule" style="left:565px;top:2102px"></div>
  <div class="review-card"></div>

  <div class="review" style="left:122px">
    <div class="stars"><svg width="22" height="20"><use href="#star"/></svg><svg width="22" height="20"><use href="#star"/></svg><svg width="22" height="20"><use href="#star"/></svg><svg width="22" height="20"><use href="#star"/></svg><svg width="22" height="20"><use href="#star"/></svg></div>
    <p>Lorem ipsum dolor sit amet, consectetur adipiscing elit, sed do eiusmod tempor incididunt ut labore et dolore magna aliqua. Quis ipsum suspendisse ultrices gravida. Risus commodo viverra maece-nas accumsan lacus vel facilisis.</p>
  </div>
  <div class="review" style="left:461px">
    <div class="stars"><svg width="22" height="20"><use href="#star"/></svg><svg width="22" height="20"><use href="#star"/></svg><svg width="22" height="20"><use href="#star"/></svg><svg width="22" height="20"><use href="#star"/></svg><svg width="22" height="20"><use href="#star"/></svg></div>
    <p>Lorem ipsum dolor sit amet, consectetur adipiscing elit, sed do eiusmod tempor incididunt ut labore et dolore magna aliqua. Quis ipsum suspendisse ultrices gravida. Risus commodo viverra maece-nas accumsan lacus vel facilisis.</p>
  </div>
  <div class="review" style="left:799px">
    <div class="stars"><svg width="22" height="20"><use href="#star"/></svg><svg width="22" height="20"><use href="#star"/></svg><svg width="22" height="20"><use href="#star"/></svg><svg width="22" height="20"><use href="#star"/></svg><svg width="22" height="20"><use href="#star"/></svg></div>
    <p>Lorem ipsum dolor sit amet, consectetur adipiscing elit, sed do eiusmod tempor incididunt ut labore et dolore magna aliqua. Quis ipsum suspendisse ultrices gravida. Risus commodo viverra maece-nas accumsan lacus vel facilisis.</p>
  </div>

  <div class="author" style="left:120px"><div class="avatar" role="img" aria-label="Client portrait"></div><div><b>MORGAN ELLISON</b><small>Lorem Ipsum</small></div></div>
  <div class="author" style="left:459px"><div class="avatar" role="img" aria-label="Client portrait"></div><div><b>MORGAN ELLISON</b><small>Lorem Ipsum</small></div></div>
  <div class="author" style="left:797px"><div class="avatar" role="img" aria-label="Client portrait"></div><div><b>MORGAN ELLISON</b><small>Lorem Ipsum</small></div></div>
</section>

<svg width="0" height="0" style="position:absolute">
  <defs><symbol id="star" viewBox="0 0 22 20"><polygon points="11,0 13.6,7 21,7.3 15.2,12 17.3,19.5 11,15.2 4.7,19.5 6.8,12 1,7.3 8.4,7" fill="#eaa623"/></symbol></defs>
</svg>

<!-- contact -->
<section>
  <div class="contact"></div>
  <h2 class="h2" style="left:0;width:1200px;text-align:center;top:2612px">CONTACT US</h2>
  <div class="rule" style="left:565px;top:2666px"></div>

  <div class="info-icon" style="top:2715px"><svg width="16" height="20" viewBox="0 0 16 20"><path d="M8 0a7 7 0 0 0-7 7c0 5 7 13 7 13s7-8 7-13a7 7 0 0 0-7-7z" fill="#eaa623"/><circle cx="8" cy="7" r="2.5" fill="#fff"/></svg></div>
  <div class="info-title" style="top:2711px">LOCATION</div>
  <div class="info-text" style="top:2742px">Lorem ipsum dolor sit amet, con-sectetur adipiscing elit</div>

  <div class="info-icon" style="top:2821px"><svg width="16" height="16" viewBox="0 0 24 24"><path fill="#eaa623" d="M6.6 10.8a15.1 15.1 0 0 0 6.6 6.6l2.2-2.2c.3-.3.7-.4 1-.2 1.1.4 2.3.6 3.6.6.6 0 1 .4 1 1V20c0 .6-.4 1-1 1A17 17 0 0 1 3 4c0-.6.4-1 1-1h3.5c.6 0 1 .4 1 1 0 1.3.2 2.5.6 3.6.1.3 0 .7-.2 1z"/></svg></div>
  <div class="info-title" style="top:2816px">PHONE</div>
  <div class="info-text" style="top:2846px">+1 888 888 8888</div>

  <div class="info-icon" style="top:2916px"><svg width="18" height="14" viewBox="0 0 16 12"><rect width="16" height="12" rx="1" fill="#eaa623"/><path d="M0 1l8 6 8-6" stroke="#fff" stroke-width="1.5" fill="none"/></svg></div>
  <div class="info-title" style="top:2911px">EMAIL</div>
  <div class="info-text" style="top:2942px;width:300px">info@keystoneledgerinc.com</div>

  <div class="field" style="top:2716px">Name</div>
  <div class="field" style="top:2783px">Phone</div>
  <div class="field" style="top:2850px">Email</div>
  <div class="submit">SUBMIT</div>
  <div class="message">Type your message</div>
</section>

<!-- footer -->
<footer>
  <div class="footer"></div>
  <svg class="footer-edge" width="1200" height="160" viewBox="0 3035 1200 160">
    <polygon points="0,3035 421,3185 557,3098 617,3103 680,3134 841,3028 911,3115 1200,3035" fill="#eaa623"/>
    <polygon points="0,3035 0,3022 421,3172 557,3085 617,3090 680,3121 841,3015 911,3102 1200,3022 1200,3035 911,3115 841,3028 680,3134 617,3103 557,3098 421,3185" fill="#eaa623"/>
    <polygon points="0,3035 1200,3035 1200,3022 911,3102 841,3015 680,3121 617,3090 557,3085 421,3172 0,3022" fill="#f4f4f4"/>
  </svg>
  <div class="badge" style="left:556px;top:3068px"><i></i></div>

  <div class="footer-brand"><span class="brand-dot"></span>Keystone Ledger</div>
  <div class="social" style="left:112px"></div>
  <div class="social" style="left:151px"></div>
  <div class="social" style="left:190px"></div>
  <div class="social" style="left:229px"></div>

  <div class="f-head" style="left:387px">QUICK LINK</div>
  <div class="f-rule" style="left:387px"></div>
  <ul class="f-links" style="left:389px"><li>Home</li><li>About Us</li><li>Our Services</li><li>Who we Are</li><li>Contact Us</li><li>More</li></ul>

  <div class="f-head" style="left:563px">SUPPORT</div>
  <div class="f-rule" style="left:563px"></div>
  <ul class="f-links" style="left:565px"><li>Terms &amp; Conditions</li><li>Privacy Policy</li><li>About Us</li><li>Support</li></ul>

  <div class="f-head" style="left:761px">SUBSCRIBE TO OUR NEWSLETTER</div>
  <div class="f-rule" style="left:761px"></div>
  <p class="f-text">Lorem ipsum dolor sit amet, consectetur adipiscing elit, sed do</p>
  <div class="subscribe">Enter Your Email</div>
  <div class="subscribe-btn"><svg width="18" height="18" viewBox="0 0 18 18"><polygon points="1,8 17,1 11,17 8,10" fill="#fff"/></svg></div>

  <div class="f-divider"></div>
  <p class="copyright">©Copyrights 2022 <a>Keystone Ledger Group, Inc</a> &nbsp;|&nbsp; All Rights Reserved</p>
</footer>

</body>
</html>
```